Business Card Design Project

Our slogan is "Made for the outside" and we are after something creative and different to go with our company image.

Criteria:
The business card will not be a standard size but it must be small or big enough to fit in a wallet.
It will be double sided
It will have our colours and the design will be based around our logo (attached)
No fancy text just clean sharp easy to read. we have been using the stag sans book font type so this or similar type is preferable (we are not locked in a font type.

For more information about us, please visit out website at www.glimtrovale.com.au

Target Market(s)

outdoor and recreational industry/market

Industry/Entity Type

Business

Requirements
Must have
• Logo
Slogan
website
contact details (phone and email)
Name and Position
social media facebook and youtube

```html
<!DOCTYPE html>
<html lang="en">
<head>
<meta charset="utf-8">
<title>Glimtrovale Business Card</title>
<link rel="stylesheet" href="https://fonts.googleapis.com/css2?family=Questrial&family=Allura&display=swap">
<style>
  :root {
    --backdrop: #d9d6d3;
    --card-top: #252525;
    --card-bottom: #0b0b0b;
    --brand-red: #e5261b;
    --line-red: #b81c14;
    --text-white: #f4f4f4;
    --text-soft: #d8d8d8;
  }
  * { box-sizing: border-box; margin: 0; padding: 0; }
  html, body {
    width: 1200px; height: 900px; overflow: hidden;
    background: var(--backdrop);
    font-family: "Questrial", "Helvetica Neue", Arial, sans-serif;
  }
  .canvas { position: relative; width: 1200px; height: 900px; }
  .card {
    position: absolute; left: 320px;
    width: 560px; height: 320px;
    background: linear-gradient(180deg, var(--card-top), var(--card-bottom));
    box-shadow: 0 8px 24px rgba(0,0,0,0.25);
    overflow: hidden;
    color: var(--text-white);
  }
  .card--front { top: 100px; }
  .card--back { top: 480px; }

  /* front */
  .front-mark {
    position: absolute; left: 50%; top: 34px;
    width: 112px; height: 112px; margin-left: -56px;
    border: 5px solid var(--brand-red); border-radius: 50%;
  }
  .front-name {
    position: absolute; left: 0; right: 0; top: 162px;
    text-align: center; font-size: 38px; letter-spacing: 4px;
    color: var(--text-white);
  }
  .front-slogan {
    position: absolute; left: 0; right: 0; top: 212px;
    text-align: center; font-size: 11px; letter-spacing: 2.5px;
    color: var(--text-white);
  }
  .front-web {
    position: absolute; left: 0; right: 0; top: 262px;
    text-align: center; font-size: 11px; letter-spacing: 1.5px;
    color: var(--brand-red);
  }
  .front-rule {
    position: absolute; left: 0; right: 0; top: 282px;
    height: 1px; background: var(--line-red);
  }

  /* back */
  .back-brand {
    position: absolute; left: 250px; top: 34px;
    display: flex; align-items: center; gap: 12px;
  }
  .back-brand__mark {
    width: 52px; height: 52px;
    border: 4px solid var(--brand-red); border-radius: 50%;
  }
  .back-brand__name {
    font-size: 24px; letter-spacing: 3px; color: var(--text-white);
  }
  .holder { position: absolute; left: 40px; top: 104px; }
  .holder__name {
    font-family: "Allura", "Brush Script MT", cursive;
    font-size: 46px; line-height: 1; color: var(--text-white);
  }
  .holder__name-last { color: var(--brand-red); }
  .holder__role { font-size: 19px; color: var(--text-white); margin-top: 4px; }
  .back-rule { position: absolute; left: 0; right: 0; height: 1px; background: var(--line-red); }
  .back-rule--upper { top: 238px; }
  .back-rule--lower { top: 299px; }
  .contact-list {
    position: absolute; top: 248px; list-style: none;
    font-size: 12px; letter-spacing: 0.5px; color: var(--text-soft);
  }
  .contact-list--left { left: 30px; }
  .contact-list--right { right: 40px; }
  .contact-list li { display: flex; align-items: center; gap: 8px; height: 20px; }
  .contact-icon { flex: none; }
  .back-slogan { position: absolute; left: 0; right: 0; top: 292px; text-align: center; }
  .back-slogan span {
    display: inline-block; padding: 0 10px;
    background: #0d0d0d;
    font-size: 10px; letter-spacing: 2.5px; color: var(--brand-red);
  }
</style>
</head>
<body>
<main class="canvas">

  <section class="card card--front" aria-label="Card front">
    <div class="front-mark"></div>
    <div class="front-name">GLIMTROVALE</div>
    <div class="front-slogan">MADE FOR THE OUTSIDE</div>
    <div class="front-web">WWW.GLIMTROVALE.COM.AU</div>
    <div class="front-rule"></div>
  </section>

  <section class="card card--back" aria-label="Card back">
    <div class="back-brand">
      <div class="back-brand__mark"></div>
      <div class="back-brand__name">GLIMTROVALE</div>
    </div>

    <div class="holder">
      <div class="holder__name">Mara <span class="holder__name-last">Quellen</span></div>
      <div class="holder__role">Head of Operations</div>
    </div>

    <div class="back-rule back-rule--upper"></div>

    <ul class="contact-list contact-list--left">
      <li>
        <svg class="contact-icon" width="14" height="10" viewBox="0 0 14 10" aria-hidden="true"><path d="M1 9 L7 2 L13 9" fill="none" stroke="#e5261b" stroke-width="1.6"/></svg>
        www.glimtrovale.com.au
      </li>
      <li>
        <svg class="contact-icon" width="14" height="10" viewBox="0 0 14 10" aria-hidden="true"><path d="M1 9 L7 2 L13 9" fill="none" stroke="#e5261b" stroke-width="1.6"/></svg>
        enquiries@glimtrovale.com.au
      </li>
    </ul>

    <ul class="contact-list contact-list--right">
      <li>
        <svg class="contact-icon" width="12" height="12" viewBox="0 0 12 12" aria-hidden="true"><rect width="12" height="12" fill="#e5261b"/></svg>
        @glimtrovale/info
      </li>
      <li>
        <svg class="contact-icon" width="12" height="12" viewBox="0 0 12 12" aria-hidden="true"><rect width="12" height="12" fill="#e5261b"/></svg>
        @theglimtrovale
      </li>
    </ul>

    <div class="back-rule back-rule--lower"></div>
    <div class="back-slogan"><span>MADE FOR THE OUTSIDE</span></div>
  </section>

</main>
</body>
</html>
```